Investment fund letterhead + bus.card design

We are an investment fund focused on investments in the energy sector.
Pls. use design of existing logo in the attachment.
You are free to change the colors of the logo.
However, some associations should exist on the website as well.
webpage: www.brightelmholdings.fund.
This is a contest for a letterhead and business card. Therefore, pls. present letterhead and business card at once. The winner will be selected by January 11, 12pm.

Good luck! Good luck! Good luck! Good luck! Good luck! Good luck! Good luck! Good luck! Good luck! Good luck! Good luck! Good luck! Good luck! Good luck! Good luck! Good luck! Good luck! Good luck! Good luck! Good luck! Good luck! Good luck! Good luck! Good luck! Good luck! Good luck! Good luck! Good luck! Good luck! Good luck! Good luck! Good luck! Good luck! Good luck! Good luck! Good luck! Good luck! Good luck! Good luck! Good luck! Good luck! Good luck! Good luck! Good luck! Good luck! Good luck! Good luck! Good luck! Good luck! Good luck! Good luck! Good luck! Good luck! Good luck! Good luck! Good luck! Good luck! Good luck! Good luck! Good luck! Good luck! Good luck! Good luck! Good luck! Good luck! Good luck! Good luck! Good luck! Good luck! Good luck! Good luck! Good luck! Good luck! Good luck! Good luck! Good luck! Good luck! Good luck! Good luck! Good luck! Good luck! Good luck! Good luck! Good luck! Good luck! Good luck! Good luck! Good luck! Good luck! Good luck! Good luck! Good luck! Good luck! Good luck! Good luck! Good luck! Good luck! Good luck! Good luck! Good luck! Good luck! Good luck! Good luck! Good luck! Good luck! Good luck! Good luck! Good luck! Good luck! Good luck! Good luck! Good luck! Good luck! Good luck! Good luck! Good luck! Good luck! Good luck! Good luck! Good luck! Good luck! Good luck! Good luck! Good luck! Good luck! Good luck! Good luck! Good luck! Good luck! Good luck! Good luck! Good luck! Good luck! Good luck! Good luck! Good luck! Good luck! Good luck! Good luck! Good luck! Good luck! Good luck! Good luck! Good luck! Good luck! Good luck! Good luck! Good luck! Good luck! Good luck! Good luck! Good luck! Good luck! Good luck! Good luck! Good luck! Good luck! Good luck! Good luck! Good luck! Good luck! Good luck! Good luck! Good luck! Good luck! Good luck! Good luck! Good luck! Good luck! Good luck! Good luck! Good luck! Good luck! Good luck! Good luck! Good luck! Good luck! Good luck! Good luck! Good luck! Good luck! Good luck! Good luck! Good luck! Good luck! Good luck! Good luck! Good luck! Good luck! Good luck! Good luck! Good luck! Good luck! Good luck! Good luck! Good luck! Good luck! Good luck! Good luck! Good luck! Good luck! Good luck! Good luck! Good luck! Good luck! Good luck! Good luck! Good luck! Good luck! Good luck! Good luck! Good luck! Good luck! Good luck! Good luck! Good luck! Good luck! Good luck! Good luck! Good luck! Good luck! Good luck! Good luck! Good luck! Good luck! Good luck! Good luck! Good luck! Good luck! Good luck! Good luck! Good luck! Good luck! Good luck! Good luck! Good luck! Good luck! Good luck! Good luck! Good luck! Good luck! Good luck! Good luck!

Target Market(s)

Energy companies, Financial institutions

Industry/Entity Type

Investment Banking

Contact Information for Business Card

Title, Name, contacts

Font styles to use
Serif

Colors

Designer to choose colors to be used in the design.

Requirements
Must have
• Logo
Nice to have
• Some modern design hints/design elements.

```html
<!DOCTYPE html>
<html lang="en">
<head>
<meta charset="utf-8">
<title>Bright Elm Holdings — Business Card</title>
<link rel="stylesheet" href="https://fonts.googleapis.com/css2?family=Arimo:wght@400;700&display=swap">
<style>
  :root {
    --backdrop: #e3e3e3;
    --navy: #04233f;
    --navy-rule: #1b3a57;
    --accent-blue: #1c5f98;
    --name-blue: #2b74b8;
    --steel-grey: #7c7c7c;
    --paper: #efefef;
    --white: #ffffff;
  }
  html, body {
    margin: 0;
    width: 1200px;
    height: 863px;
    overflow: hidden;
    background: var(--backdrop);
    font-family: "Arimo", Arial, sans-serif;
  }
  .canvas { position: relative; width: 1200px; height: 863px; }
  .card {
    position: absolute;
    left: 350px;
    width: 500px;
    height: 279px;
    box-shadow: 0 1px 3px rgba(0,0,0,0.18);
  }
  .card--front { top: 114px; }
  .card--back { top: 470px; }
  .card svg { display: block; width: 100%; height: 100%; }
  .name { fill: var(--name-blue); font-weight: 700; font-size: 20px; }
  .job-title { fill: var(--white); font-size: 16px; }
  .contact { fill: var(--white); font-size: 14.5px; }
  .wordmark { fill: var(--navy); font-weight: 700; font-size: 14px; letter-spacing: 1.6px; }
  .wordmark--back { fill: var(--white); font-size: 20px; letter-spacing: 2.6px; }
  .band-url { fill: var(--navy); font-weight: 700; font-size: 14px; letter-spacing: 1.6px; }
  .icon { fill: none; stroke: var(--white); stroke-width: 2; stroke-linecap: round; stroke-linejoin: round; }
  .icon--solid { fill: var(--white); stroke: none; }
</style>
</head>
<body>
<main class="canvas">

  <section class="card card--front" aria-label="Business card front">
    <svg viewBox="0 0 626 348" xmlns="http://www.w3.org/2000/svg">
      <rect class="paper" width="626" height="348" fill="var(--paper)"/>
      <polygon class="contact-panel" points="0,0 240,0 331,348 0,348" fill="var(--navy)"/>
      <polygon class="divider-stripe" points="240,0 250,0 341,348 331,348" fill="var(--steel-grey)"/>

      <line x1="0" y1="207" x2="294" y2="207" stroke="var(--navy-rule)" stroke-width="1.2"/>
      <line x1="0" y1="259" x2="308" y2="259" stroke="var(--navy-rule)" stroke-width="1.2"/>

      <polygon class="icon-tab" points="229,153 280,153 293.6,205 242.6,205" fill="var(--accent-blue)"/>
      <polygon class="icon-tab" points="243,207 294,207 307,257 256,257" fill="var(--accent-blue)"/>
      <polygon class="icon-tab" points="257,261 308,261 320.6,309 269.6,309" fill="var(--accent-blue)"/>

      <g transform="translate(261,180)">
        <path class="icon--solid" d="M-12,1 L0,-10 L12,1 L9,1 L9,10 L3,10 L3,4 L-3,4 L-3,10 L-9,10 L-9,1 Z"/>
      </g>
      <g transform="translate(275,232)">
        <path class="icon--solid" d="M-6,-11 C-8,-11 -9,-9 -9,-6 C-9,2 -3,10 5,12 C8,12 10,11 10,9 L10,6 L4,4 L2,7 C-2,5 -4,1 -5,-3 L-2,-5 L-4,-11 Z"/>
      </g>
      <g class="icon" transform="translate(289,285)">
        <circle r="10"/>
        <ellipse rx="4.5" ry="10"/>
        <line x1="-10" y1="0" x2="10" y2="0"/>
        <path d="M-8.5,-5 H8.5 M-8.5,5 H8.5"/>
      </g>

      <text class="name" x="45" y="71">PAVEL SOROKIN</text>
      <text class="job-title" x="44" y="93">General Manager</text>

      <text class="contact" x="44" y="176">Moscow</text>
      <text class="contact" x="44" y="196">Energetikov str, 4-12</text>
      <text class="contact" x="44" y="228">+7 000 555 0142</text>
      <text class="contact" x="44" y="248">+7 000 555 0142</text>
      <text class="contact" x="44" y="280">contact@brightelm.fund</text>
      <text class="contact" x="44" y="300">www.brightelmholdings.fund</text>

      <rect class="brand-mark" x="426" y="116" width="76" height="76" fill="var(--navy)"/>
      <text class="wordmark" x="464" y="233" text-anchor="middle">BRIGHT ELM HOLDINGS</text>
    </svg>
  </section>

  <section class="card card--back" aria-label="Business card back">
    <svg viewBox="0 0 626 349" xmlns="http://www.w3.org/2000/svg">
      <rect width="626" height="349" fill="var(--navy)"/>
      <polygon class="url-band-stripe" points="374,154 385,154 396,205 385,205" fill="var(--steel-grey)"/>
      <polygon class="url-band" points="385,154 626,154 626,205 396,205" fill="var(--accent-blue)"/>
      <text class="wordmark wordmark--back" x="46" y="189">BRIGHT ELM HOLDINGS</text>
      <text class="band-url" x="506" y="184" text-anchor="middle">brightelmholdings.fund</text>
    </svg>
  </section>

</main>
</body>
</html>
```